Business Card Design for Tidewell

The company provides engineering tender consulting services and personnel resources. The target market is large engineering construction and services companies. The business is based in Australia.

```html
<!DOCTYPE html>
<html lang="en">
<head>
<meta charset="utf-8">
<title>Tidewell — Business Card</title>
<link rel="stylesheet" href="https://fonts.googleapis.com/css2?family=Fira+Sans:wght@300;400&display=swap">
<style>
  :root {
    --bg-left: #241810;
    --bg-right: #4d2a05;
    --card-light: #f6f6f6;
    --card-shade: #e4e4e4;
    --ink: #161616;
    --rule: #7a7a7a;
    --mark: #333333;
    --panel-blue: #2e8ff7;
    --panel-blue-deep: #2679d6;
  }
  * { margin: 0; padding: 0; box-sizing: border-box; }
  html, body {
    width: 1200px;
    height: 849px;
    overflow: hidden;
  }
  body {
    position: relative;
    background: linear-gradient(90deg, var(--bg-left), var(--bg-right));
    font-family: "Fira Sans", sans-serif;
    color: var(--ink);
  }
  .card {
    position: absolute;
    left: 138px;
    top: 144px;
    width: 924px;
    height: 559px;
    background: linear-gradient(90deg, var(--card-light), var(--card-shade));
    overflow: hidden;
  }
  .brand-square {
    position: absolute;
    left: 30px;
    top: 36px;
    width: 124px;
    height: 123px;
    background: var(--mark);
  }
  .brand-name {
    position: absolute;
    left: 158px;
    top: 40px;
    font-size: 68px;
    line-height: 1;
    font-weight: 400;
    letter-spacing: 0.5px;
  }
  .slogan {
    position: absolute;
    left: 222px;
    top: 117px;
    font-size: 30px;
    line-height: 1;
    font-weight: 400;
  }
  .slogan-rule {
    position: absolute;
    left: 209px;
    top: 156px;
    width: 351px;
    height: 2px;
    background: var(--rule);
  }
  .person-name {
    position: absolute;
    left: 134px;
    top: 231px;
    font-size: 44px;
    line-height: 1;
    font-weight: 400;
  }
  .contact {
    position: absolute;
    left: 76px;
    top: 339px;
    display: grid;
    grid-template-columns: 102px auto;
    column-gap: 31px;
    font-size: 30px;
    line-height: 35px;
    font-weight: 400;
  }
  .contact-divider {
    position: absolute;
    left: 178px;
    top: 343px;
    width: 1.5px;
    height: 136px;
    background: var(--rule);
  }
  .contact-underline {
    position: absolute;
    left: 76px;
    top: 478px;
    width: 102px;
    height: 1.5px;
    background: var(--rule);
  }
  .abn {
    position: absolute;
    left: 76px;
    top: 492px;
    font-size: 30px;
    line-height: 1;
  }
  .brand-panel {
    position: absolute;
    left: 647px;
    top: 0;
    width: 277px;
    height: 559px;
    border-top-left-radius: 10px;
    background: linear-gradient(160deg, var(--panel-blue), var(--panel-blue-deep));
  }
</style>
</head>
<body>
  <main class="card">
    <div class="brand-square"></div>
    <h1 class="brand-name">Tidewell</h1>
    <p class="slogan">Slogan Abcd Efgh Mnop</p>
    <div class="slogan-rule"></div>

    <p class="person-name">Firstname Surname</p>

    <div class="contact">
      <span class="contact-label">Tel</span><span class="contact-value">0123 456 789</span>
      <span class="contact-label">Mobile</span><span class="contact-value">0123 456 789</span>
      <span class="contact-label">Email</span><span class="contact-value">abcde@nnn.com.au</span>
      <span class="contact-label">PO Box</span><span class="contact-value">99 Nnnnnnnnnn, Nnn, 9999</span>
    </div>
    <div class="contact-divider"></div>
    <div class="contact-underline"></div>
    <p class="abn">ABN9999999999</p>

    <div class="brand-panel" role="img" aria-label="Decorative brand panel: enlarged company symbol in blue, green, black and white"></div>
  </main>
</body>
</html>
```